physical therapy flyer

2 office locations speciality programs - work injury / Motor vehicle accidents - spanish speaking - do not put balance defecits/ fall prevention - Spanish speaking
neck and back pain shoulder pain/ rotator cuff disorder / bursitis
hip pain knee andle and foot pain post operative care including Spine , shoulder , knee , total joint replacement

Meadowlark Physical therapy & Chiropractic
4827 Ashbury BLvd
lindell park ny 11592
7185528174
3719 Tillman Parkway
Corvale NY 11592
7182947061
www.meadowlarkptchiroacu.com

```html
<!DOCTYPE html>
<html lang="en">
<head>
<meta charset="utf-8">
<title>Meadowlark Physical Therapy &amp; Chiropractic Flyer</title>
<link href="https://fonts.googleapis.com/css2?family=Poppins:wght@300;400;500;600;700&display=swap" rel="stylesheet">
<style>
:root{
  --backdrop:#58585a;
  --ink-dark:#262628;
  --ink-dark-2:#3a3a3d;
  --green-deep:#1d7a3a;
  --green:#2e9a4a;
  --green-bright:#3fae49;
  --green-light:#76bf43;
  --green-pale:#8fd3a6;
  --white:#ffffff;
  --text-dark:#1d1d1d;
  --text-grey:#444;
}
*{margin:0;padding:0;box-sizing:border-box}
html,body{width:1200px;height:2192px;overflow:hidden;background:var(--backdrop)}
body{font-family:"Poppins",sans-serif;position:relative}
.flyer-frame{position:absolute;left:60px;top:398px;width:1080px;height:1397px;box-shadow:0 20px 50px rgba(0,0,0,.45);overflow:hidden}
.flyer{position:absolute;left:0;top:0;width:897px;height:1160px;transform:scale(1.204);transform-origin:0 0;background:var(--white);overflow:hidden}
.flyer-shapes{position:absolute;left:0;top:0;width:897px;height:1160px}
.brand{position:absolute;left:64px;top:96px;display:flex;align-items:center;gap:14px;color:var(--white)}
.brand-mark{width:54px;height:54px;border-radius:50%;border:2px solid var(--white)}
.brand-name{font-weight:300;font-size:21px;line-height:1.2}
.headline{position:absolute;left:62px;color:var(--white);font-weight:600;font-size:50px;line-height:48px;letter-spacing:.3px}
.headline.first{top:228px}
.headline.second{top:460px}
.badge{position:absolute;left:62px;width:300px;height:42px;background:var(--green-light);color:var(--white);font-weight:600;font-size:26px;line-height:42px;text-align:center;border-radius:3px}
.badge.first{top:384px}
.badge.second{top:621px}
.conditions{position:absolute;left:62px;top:734px;display:grid;grid-template-columns:213px auto;row-gap:7px;font-size:16px;color:var(--text-grey)}
.conditions li{list-style:none;display:flex;align-items:center;gap:7px;height:22px}
.tick{width:17px;height:17px;flex:none}
.band-label{position:absolute;left:62px;font-weight:600}
.post-op-title{top:843px;font-size:19px;color:var(--text-dark)}
.post-op-list{top:884px;font-size:16px;color:var(--white)}
.clinic-name{top:928px;font-size:23px;color:var(--white);font-weight:700}
.location{position:absolute;top:992px;color:var(--white)}
.location.one{left:62px}
.location.two{left:362px}
.address{display:flex;gap:14px;font-size:17px;line-height:26px}
.phone{display:flex;gap:14px;align-items:center;margin-top:12px;font-size:23px;font-weight:600}
.icon{width:22px;height:26px;flex:none}
.website{position:absolute;left:62px;top:1098px;color:var(--green-bright);font-size:18px;font-weight:500}
</style>
</head>
<body>
<div class="flyer-frame">
<div class="flyer">
  <svg class="flyer-shapes" viewBox="0 0 897 1160" xmlns="http://www.w3.org/2000/svg">
    <defs>
      <linearGradient id="darkBand" x1="0" y1="0" x2="1" y2="0">
        <stop offset="0" stop-color="#333336"/><stop offset="1" stop-color="#1f1f21"/>
      </linearGradient>
      <linearGradient id="greenPanel" x1="0" y1="0" x2="1" y2="1">
        <stop offset="0" stop-color="#2d8a4c"/><stop offset=".5" stop-color="#1f7a3d"/><stop offset="1" stop-color="#2a9447"/>
      </linearGradient>
      <linearGradient id="crashPhoto" x1="0" y1="0" x2="1" y2="1">
        <stop offset="0" stop-color="#c9ccc9"/><stop offset=".5" stop-color="#7d848a"/><stop offset="1" stop-color="#a19a90"/>
      </linearGradient>
      <linearGradient id="kneePhoto" x1="0" y1="0" x2="1" y2="1">
        <stop offset="0" stop-color="#c8c9c7"/><stop offset=".5" stop-color="#8a6a5a"/><stop offset="1" stop-color="#d9d6d2"/>
      </linearGradient>
      <radialGradient id="shoulderPhoto" cx=".45" cy=".4" r=".6">
        <stop offset="0" stop-color="#e0564e"/><stop offset=".45" stop-color="#e8b4a6"/><stop offset="1" stop-color="#e4e4e4"/>
      </radialGradient>
    </defs>
    <rect x="0" y="0" width="897" height="195" fill="url(#darkBand)"/>
    <path d="M0 195 H897 V560 L845 585 L845 600 Q760 700 560 712 H0 Z" fill="url(#greenPanel)" role="img" aria-label="Green-tinted photo of a damaged bicycle after a collision"/>
    <rect x="0" y="192" width="500" height="4" fill="var(--green-bright)"/>
    <path d="M700 600 L845 580 L845 720 L640 720 Z" fill="#1e1e20"/>
    <rect x="0" y="838" width="897" height="40" fill="var(--green-light)"/>
    <rect x="0" y="876" width="897" height="44" fill="var(--green)"/>
    <rect x="0" y="920" width="897" height="52" fill="#111"/>
    <rect x="0" y="972" width="897" height="118" fill="var(--green)"/>
    <circle cx="775" cy="212" r="318" fill="var(--green-pale)"/>
    <circle cx="770" cy="208" r="305" fill="var(--green-bright)"/>
    <circle cx="772" cy="200" r="290" fill="url(#crashPhoto)" role="img" aria-label="Photo of a distressed man crouching beside a wrecked car"/>
    <circle cx="693" cy="790" r="180" fill="var(--green-bright)"/>
    <circle cx="696" cy="792" r="168" fill="url(#kneePhoto)" role="img" aria-label="Photo of hands holding a painful knee"/>
    <circle cx="818" cy="1042" r="155" fill="#cfe9c4"/>
    <circle cx="822" cy="1046" r="140" fill="url(#shoulderPhoto)" role="img" aria-label="Photo of a hand on a red, painful shoulder"/>
  </svg>

  <div class="brand">
    <span class="brand-mark"></span>
    <p class="brand-name">Meadowlark Physical Therapy,<br>Chiropractic, and Acupuncture</p>
  </div>

  <h1 class="headline first">WORK INJURY<br>MOTOR VEHICLE<br>ACCIDENTS</h1>
  <p class="badge first">SPANISH SPEAKING</p>
  <h2 class="headline second">DO NOT PUT<br>BALANCE DEFECITS<br>FALL PREVENTION</h2>
  <p class="badge second">SPANISH SPEAKING</p>

  <ul class="conditions">
    <li><svg class="tick" viewBox="0 0 17 17"><rect x="1" y="3" width="13" height="13" fill="none" stroke="#3fae49" stroke-width="1.5"/><path d="M4 9 L7.5 12.5 L15 2" fill="none" stroke="#3fae49" stroke-width="2"/></svg>Neck and Back Pain</li>
    <li><svg class="tick" viewBox="0 0 17 17"><rect x="1" y="3" width="13" height="13" fill="none" stroke="#3fae49" stroke-width="1.5"/><path d="M4 9 L7.5 12.5 L15 2" fill="none" stroke="#3fae49" stroke-width="2"/></svg>Bursitis</li>
    <li><svg class="tick" viewBox="0 0 17 17"><rect x="1" y="3" width="13" height="13" fill="none" stroke="#3fae49" stroke-width="1.5"/><path d="M4 9 L7.5 12.5 L15 2" fill="none" stroke="#3fae49" stroke-width="2"/></svg>Shoulder Pain</li>
    <li><svg class="tick" viewBox="0 0 17 17"><rect x="1" y="3" width="13" height="13" fill="none" stroke="#3fae49" stroke-width="1.5"/><path d="M4 9 L7.5 12.5 L15 2" fill="none" stroke="#3fae49" stroke-width="2"/></svg>Hip Pain</li>
    <li><svg class="tick" viewBox="0 0 17 17"><rect x="1" y="3" width="13" height="13" fill="none" stroke="#3fae49" stroke-width="1.5"/><path d="M4 9 L7.5 12.5 L15 2" fill="none" stroke="#3fae49" stroke-width="2"/></svg>Rotator Cuff Disorder</li>
    <li><svg class="tick" viewBox="0 0 17 17"><rect x="1" y="3" width="13" height="13" fill="none" stroke="#3fae49" stroke-width="1.5"/><path d="M4 9 L7.5 12.5 L15 2" fill="none" stroke="#3fae49" stroke-width="2"/></svg>Knee Angle and Foot Pain</li>
  </ul>

  <p class="band-label post-op-title">Post Operative Care Including:</p>
  <p class="band-label post-op-list">Spine , Shoulder , Knee , Total Joint Replacement</p>
  <p class="band-label clinic-name">MEADOWLARK PHYSICAL THERAPY &amp; CHIROPRACTIC</p>

  <div class="location one">
    <div class="address"><svg class="icon" viewBox="0 0 22 26"><path d="M11 1 C5 1 2 5 2 9.5 C2 16 11 25 11 25 C11 25 20 16 20 9.5 C20 5 17 1 11 1 Z" fill="#fff"/><circle cx="11" cy="9.5" r="3.5" fill="#2e9a4a"/></svg><p>4827 Ashbury Blvd<br>Lindell Park NY 11592</p></div>
    <div class="phone"><svg class="icon" viewBox="0 0 22 26"><path d="M5 5 L9 4 L11 9 L8.5 11 C9.5 14 11 16 14 17.5 L16 15 L21 17 L20 21 C12 22 4 14 5 5 Z" fill="#fff"/></svg><p>718-552-8174</p></div>
  </div>
  <div class="location two">
    <div class="address"><svg class="icon" viewBox="0 0 22 26"><path d="M11 1 C5 1 2 5 2 9.5 C2 16 11 25 11 25 C11 25 20 16 20 9.5 C20 5 17 1 11 1 Z" fill="#fff"/><circle cx="11" cy="9.5" r="3.5" fill="#2e9a4a"/></svg><p>3719 Tillman Parkway<br>Corvale NY 11592</p></div>
    <div class="phone"><svg class="icon" viewBox="0 0 22 26"><path d="M5 5 L9 4 L11 9 L8.5 11 C9.5 14 11 16 14 17.5 L16 15 L21 17 L20 21 C12 22 4 14 5 5 Z" fill="#fff"/></svg><p>718-294-7061</p></div>
  </div>

  <p class="website">www.meadowlarkptchiroacu.com</p>
</div>
</div>
</body>
</html>
```